Website for Vetra Kolan Holdings

Need a project marketing website for our company which primarily deals in selling real estate(land sales) from Big Estates to Builders /Clients, help them in Building & Construction and do all Project Management.

Coding

Coded - Design and coding required

Number of Pages Required

4 page

Colors
0054AA
0677BA
7BADD7
CADEEF
E8F1F8
FFC000
F8CF3A
FAE287
FDF2CF
FEFAEE

```html
<!DOCTYPE html>
<html lang="en">
<head>
<meta charset="utf-8">
<title>Contact Us | Vetra Kolan Holdings</title>
<link href="https://fonts.googleapis.com/css2?family=Montserrat:wght@400;500;600;700&family=Playfair+Display:wght@400;500&family=Poppins:wght@700&display=swap" rel="stylesheet">
<style>
:root{
  --blue-deep:#0054AA;
  --blue:#0677BA;
  --blue-soft:#7BADD7;
  --blue-pale:#CADEEF;
  --blue-mist:#E8F1F8;
  --yellow:#FFC000;
  --yellow-warm:#F8CF3A;
  --ink:#222;
  --text:#333;
  --footer:#2D323A;
  --line:#cfd3d8;
}
*{box-sizing:border-box;margin:0;padding:0}
html,body{width:899px;height:1200px;overflow:hidden;background:#fff}
body{position:relative;font-family:"Montserrat",sans-serif;color:var(--text)}
.abs{position:absolute}

/* hero */
.hero{left:0;top:0;width:899px;height:407px;
  background:linear-gradient(100deg,#e8edf1 0%,#dfe7ee 30%,#c9d3dc 50%,#8a8e9e 70%,#6d5e6a 85%,#b07a52 100%)}
.hero-line{left:106px;top:70px;width:688px;height:1px;background:rgba(255,255,255,.45)}
.brand{left:106px;top:20px;display:flex;align-items:center;gap:8px}
.brand-mark{width:22px;height:22px;background:var(--blue-deep);flex:none}
.brand-name{font-family:"Montserrat",sans-serif;font-weight:700;font-size:17px;color:var(--blue-deep);letter-spacing:.5px}
.nav{top:28px;left:538px;display:flex;gap:33px;font-size:9px;color:#fff}
.btn-start{left:730px;top:24px;width:63px;height:20px;background:var(--blue-deep);color:#fff;
  font-size:9px;font-weight:500;display:flex;align-items:center;justify-content:center;border-radius:1px}
.banner{left:106px;top:185px;width:219px;height:86px}
.banner-title{left:130px;top:208px;font-family:"Poppins",sans-serif;font-weight:700;font-size:27px;color:#fff}

/* breadcrumb */
.crumb{left:107px;top:421px;font-size:9px;color:var(--ink)}
.crumb span{margin:0 8px}
.crumb b{font-weight:700}

.page-title{left:0;width:899px;top:452px;text-align:center;font-family:"Playfair Display",serif;font-size:27px;font-weight:400;color:var(--ink)}
.page-title em{font-style:normal;color:var(--blue-deep)}
.sec-title{top:510px;font-family:"Playfair Display",serif;font-size:26px;font-weight:400;color:var(--blue-deep)}

/* form */
.field{left:107px;width:295px;border:1px solid var(--line);border-radius:3px;font-size:10px;color:#444;padding:0 8px;display:flex;align-items:center}
.field.msg{align-items:flex-start;padding-top:8px}
.submit{left:107px;top:784px;width:106px;height:26px;background:var(--yellow);border-radius:13px;
  font-weight:700;font-size:9.5px;color:var(--ink);display:flex;align-items:center;padding-left:15px}
.submit svg{position:absolute;right:2px;top:2px}
.divider{left:430px;top:520px;width:1px;height:305px;background:linear-gradient(var(--blue-mist),#dfe3e7,var(--blue-mist))}

/* info */
.map{left:456px;top:563px;width:342px;height:130px;border:1px solid #bbb;border-radius:6px;
  background:linear-gradient(135deg,#f3efe6,#ece8df 60%,#e6e9ee)}
.info-icon{left:454px;width:27px;height:27px;border-radius:50%;background:var(--yellow);display:flex;align-items:center;justify-content:center}
.info-text{left:488px;font-size:10px;color:var(--text);line-height:14px}
.info-text strong{color:var(--blue-deep);font-weight:700;display:block}
.phone-big{font-weight:700;color:var(--ink)}

/* footer */
.footer-shape{left:0;top:820px}
.foot-brand{left:106px;top:1010px;width:145px;display:flex;align-items:center;gap:8px}
.foot-brand .brand-mark{background:#fff;width:20px;height:20px}
.foot-brand .brand-name{color:#fff;font-size:15px;line-height:18px;font-weight:700}
.foot-rule{left:106px;top:1067px;width:145px;height:1px;background:#4d535c}
.social{top:1081px;width:21px;height:21px;border-radius:50%;background:var(--yellow)}
.foot-h{top:1004px;font-family:"Playfair Display",serif;font-size:14px;font-weight:400;color:#fff}
.foot-list{left:285px;top:1035px;list-style:none;font-size:9px;color:#fff}
.foot-list li{height:18px;display:flex;align-items:center;gap:5px}
.foot-list li::before{content:"";width:4px;height:4px;border:1.5px solid var(--blue-soft);border-radius:50%}
.foot-contact{left:407px;font-size:9px;color:#fff;display:flex;gap:8px;line-height:13px}
.news-text{left:609px;top:1036px;width:180px;font-size:9px;color:#fff;line-height:13px}
.news-input{left:609px;top:1075px;width:185px;height:26px;background:#fff;font-size:9px;color:#444;display:flex;align-items:center;padding-left:8px}
.foot-bottom-rule{left:0;top:1145px;width:899px;height:1px;background:#444a53}
.copy{left:0;width:899px;top:1166px;text-align:center;font-size:9.5px;color:#fff}
</style>
</head>
<body>

<header>
  <div class="abs hero" role="img" aria-label="Photo of business people shaking hands in a bright office"></div>
  <div class="abs hero-line"></div>
  <div class="abs brand"><span class="brand-mark"></span><span class="brand-name">VETRA KOLAN HOLDINGS</span></div>
  <nav class="abs nav"><span>Home</span><span>Services</span><span>Contact</span></nav>
  <div class="abs btn-start">Get Started</div>
  <svg class="abs banner" viewBox="0 0 219 86"><polygon points="0,0 219,0 181,86 0,86" fill="#5f95d2" opacity=".85"/></svg>
  <h1 class="abs banner-title">Contact Us</h1>
</header>

<main>
  <div class="abs crumb">Home<span>/</span><b>Contact</b></div>
  <h2 class="abs page-title"><em>Contact</em> Us</h2>

  <h3 class="abs sec-title" style="left:107px">How Can We Help You?</h3>
  <div class="abs field" style="top:563px;height:29px">Name*</div>
  <div class="abs field" style="top:600px;height:29px">Email *</div>
  <div class="abs field" style="top:637px;height:29px">Phone</div>
  <div class="abs field msg" style="top:675px;height:93px">Message *</div>
  <div class="abs submit">Submit Now
    <svg width="22" height="22" viewBox="0 0 22 22"><circle cx="11" cy="11" r="11" fill="var(--blue-deep)"/><path d="M6 11h9M11 7l4 4-4 4" stroke="#fff" stroke-width="2" fill="none" stroke-linecap="round"/></svg>
  </div>

  <div class="abs divider"></div>

  <h3 class="abs sec-title" style="left:455px">Vetra Kolan Holdings</h3>
  <div class="abs map" role="img" aria-label="Street map showing the office location"></div>

  <div class="abs info-icon" style="top:712px"><svg width="12" height="14" viewBox="0 0 12 14"><path d="M6 0a5 5 0 0 0-5 5c0 4 5 8 5 8s5-4 5-8a5 5 0 0 0-5-5z" fill="none" stroke="#111" stroke-width="1.8"/><circle cx="6" cy="5" r="1.8" fill="#111"/></svg></div>
  <div class="abs info-text" style="top:711px"><strong>Vetra Kolan Holdings</strong>48/6 Corran Parade Harlow VIC 3041</div>

  <div class="abs info-icon" style="top:748px"><svg width="12" height="12" viewBox="0 0 12 12"><path d="M2 1l2 0 1 3-1.5 1a7 7 0 0 0 3.5 3.5L8 7l3 1v2c0 1-1 1-1 1C5 11 1 7 1 2c0 0 0-1 1-1z" fill="#111"/></svg></div>
  <div class="abs info-text phone-big" style="top:755px">0455123987</div>

  <div class="abs info-icon" style="top:785px"><svg width="12" height="9" viewBox="0 0 12 9"><rect width="12" height="9" rx="1" fill="#111"/><path d="M0 1l6 4 6-4" stroke="var(--yellow)" stroke-width="1.2" fill="none"/></svg></div>
  <div class="abs info-text" style="top:791px">hello@vetrakolan.com.au</div>
</main>

<footer>
  <svg class="abs footer-shape" width="899" height="380" viewBox="0 820 899 380">
    <polygon points="0,869 275,925 0,968" fill="var(--yellow)"/>
    <polygon points="899,828 899,1200 0,1200 0,968 275,925" fill="var(--footer)"/>
  </svg>

  <div class="abs foot-brand"><span class="brand-mark"></span><span class="brand-name">VETRA KOLAN<br>HOLDINGS</span></div>
  <div class="abs foot-rule"></div>
  <div class="abs social" style="left:127px"></div>
  <div class="abs social" style="left:153px"></div>
  <div class="abs social" style="left:180px"></div>
  <div class="abs social" style="left:207px"></div>

  <h4 class="abs foot-h" style="left:285px">Quick Links</h4>
  <ul class="abs foot-list"><li>Home</li><li>Services</li><li>Contact Us</li></ul>

  <h4 class="abs foot-h" style="left:407px">Contact Details</h4>
  <div class="abs foot-contact" style="top:1036px"><svg width="11" height="13" viewBox="0 0 12 14"><path d="M6 0a5 5 0 0 0-5 5c0 4 5 8 5 8s5-4 5-8a5 5 0 0 0-5-5z" fill="none" stroke="#fff" stroke-width="1.6"/><circle cx="6" cy="5" r="1.7" fill="#fff"/></svg><span>48/6 Corran Parade Harlow<br>VIC 3041</span></div>
  <div class="abs foot-contact" style="top:1070px"><svg width="11" height="11" viewBox="0 0 12 12"><path d="M2 1l2 0 1 3-1.5 1a7 7 0 0 0 3.5 3.5L8 7l3 1v2c0 1-1 1-1 1C5 11 1 7 1 2c0 0 0-1 1-1z" fill="none" stroke="#fff" stroke-width="1.2"/></svg><span>0455123987</span></div>
  <div class="abs foot-contact" style="top:1090px"><svg width="11" height="9" viewBox="0 0 12 9"><rect width="12" height="9" rx="1" fill="#fff"/><path d="M0 1l6 4 6-4" stroke="var(--footer)" stroke-width="1.2" fill="none"/></svg><span>hello@vetrakolan.com.au</span></div>

  <h4 class="abs foot-h" style="left:609px">Newsletter Sign Up</h4>
  <p class="abs news-text">Subscribe to our newsletter to get the latest update to your inbox</p>
  <div class="abs news-input">Email address</div>

  <div class="abs foot-bottom-rule"></div>
  <p class="abs copy">© 2025 Vetra Kolan Holdings. All Rights Reserved.</p>
</footer>

</body>
</html>
```